Design for Retail Product - Resealable bag. Will also need a smaller version of the same.

DESIGN REQUIREMENTS:

- Design a 16 oz bag (approx. dimensions of 6.5" wide, by 8.5" high), that represents our unique nutritional salt.

- The design should be easily downsized to a correlating/proportionate version for a smaller 8 oz bag. (The 8oz bag may/or may not have a slightly different variation in design, but if a different design, must well alongside the 16 oz bag.) .

- If we can't fit all of the product info on the bag- we will decide what can be eliminated as we finalize designs.

- This bag will be capable of standing alone on a store shelf.

- The design color can be printed to the edges top and bottom, but we will lose approx an inch of the top of the bag (above the zipper), when the customer opens the bag.

- The design can be printed to within 1/4cm of the left and right hand edges of the bag.

- The design should convey some, but not necessarily all, of the following attributes: power, versatility, athletics, clean - as in pure/free of contaminants, nutrition, physical exertion, strength, hydration, determination.

- We use a lot of the color blue, as you see in our logo, but are open to other coordinating colors.

- There are two versions of our logo attached. One is vector but in white. I would like it to be blue as it is in the jpeg file.

- Also, there is a variety of text , that should be printed on the back of the package. It is included in the attached pdf so that you can gauge placement.

- A bar code will be printed on the bottom of the bag.

- The ingredients are of utmost importance - no color or image behind them, so that they are legible.

- You are designing a 16 oz bag, with a correlating/proportionate version for a smaller 8 oz bag. The 8oz bag may/or may not have a slightly different variation in design, but if a different design, must well alongside the 16 oz bag.

WHAT WE SELL:

- Our product, called Marrow Crest, can be used as a sports supplement (as an electrolyte replacement) and in cooking and baking.

- This will be a printed, zipper top bag, with a clear window somewhere on the front of the package, so that the customer can see what the salt looks like.

Target Market(s)

Athletes, Nutrition conscious individuals, Healthy lifestyle, Hydration

Requirements
Must have
• - Strong design element , outside of copy placement
• - Must have a window to see our product - and how it looks different than other salts on the market
• - Some kind of a blue, that coordinates well with our logo
• - Our ingredients must be very legible
Nice to have
• - Images on the package
• - more than one color, or have various shades/layers of a color
Should not have
• - not have the look or feel of a "spa"

```html
<!DOCTYPE html>
<html lang="en">
<head>
<meta charset="utf-8">
<title>Marrow Crest – 16 oz Bag Front</title>
<link rel="stylesheet" href="https://fonts.googleapis.com/css2?family=Oswald:wght@400;500;600&family=Roboto+Condensed:ital,wght@1,500&display=swap">
<style>
  :root {
    --stage: #e4e4e6;
    --brand-blue: #1aa6cf;
    --ink: #1f1f24;
    --white: #ffffff;
    --magenta: #d23aa6;
    --violet: #7a45b8;
    --sky-blue: #2f9be0;
    --night: #0d0d10;
    --photo-sky: #c9d6d6;
    --photo-hills: #4f5d52;
    --photo-rock: #3a332e;
    --salt: #eef0f2;
  }
  html, body {
    margin: 0;
    padding: 0;
    width: 1200px;
    height: 900px;
    overflow: hidden;
    background: var(--stage);
  }
  .canvas {
    position: relative;
    width: 1200px;
    height: 900px;
  }
  .bag-front {
    position: absolute;
    left: 340px;
    top: 110px;
    width: 520px;
    height: 680px;
    box-shadow: 0 12px 30px rgba(0,0,0,0.18);
  }
  .claims-text {
    font-family: "Oswald", sans-serif;
    font-weight: 400;
    font-size: 22px;
    fill: var(--white);
    letter-spacing: 0.2px;
  }
  .brand-name {
    font-family: "Oswald", sans-serif;
    font-weight: 600;
    font-size: 60px;
    fill: var(--brand-blue);
    letter-spacing: 1px;
  }
  .tagline {
    font-family: "Oswald", sans-serif;
    font-weight: 400;
    font-size: 24px;
    fill: var(--ink);
  }
  .badge-figure {
    font-family: "Oswald", sans-serif;
    font-weight: 600;
    font-size: 40px;
    fill: var(--white);
  }
  .badge-label {
    font-family: "Oswald", sans-serif;
    font-weight: 500;
    font-size: 15px;
    fill: var(--white);
    letter-spacing: 0.5px;
  }
  .net-weight {
    font-family: "Roboto Condensed", sans-serif;
    font-style: italic;
    font-weight: 500;
    font-size: 30px;
    fill: var(--white);
  }
</style>
</head>
<body>
<main class="canvas">
  <svg class="bag-front" viewBox="0 0 520 680" xmlns="http://www.w3.org/2000/svg">
    <defs>
      <linearGradient id="claims-band-fill" x1="0" y1="0" x2="1" y2="0">
        <stop offset="0" stop-color="var(--magenta)"/>
        <stop offset="1" stop-color="var(--violet)"/>
      </linearGradient>
      <linearGradient id="hikers-photo-fill" x1="0" y1="0" x2="0" y2="1">
        <stop offset="0" stop-color="#e3eaea"/>
        <stop offset="0.35" stop-color="var(--photo-sky)"/>
        <stop offset="0.6" stop-color="var(--photo-hills)"/>
        <stop offset="0.85" stop-color="var(--photo-rock)"/>
        <stop offset="1" stop-color="var(--night)"/>
      </linearGradient>
      <linearGradient id="window-ring-stroke" x1="0" y1="1" x2="1" y2="0">
        <stop offset="0" stop-color="var(--magenta)"/>
        <stop offset="1" stop-color="var(--violet)"/>
      </linearGradient>
      <linearGradient id="sodium-badge-fill" x1="0" y1="0" x2="1" y2="0">
        <stop offset="0" stop-color="var(--sky-blue)"/>
        <stop offset="1" stop-color="var(--violet)"/>
      </linearGradient>
      <linearGradient id="base-band-fill" x1="0" y1="0" x2="0" y2="1">
        <stop offset="0" stop-color="rgba(13,13,16,0)"/>
        <stop offset="0.45" stop-color="var(--night)"/>
        <stop offset="1" stop-color="var(--night)"/>
      </linearGradient>
    </defs>

    <!-- background scene -->
    <rect class="hikers-photo" role="img" aria-label="Photo of two hikers with backpacks on a mountain ledge overlooking a green valley" x="0" y="0" width="520" height="680" fill="url(#hikers-photo-fill)"/>

    <!-- claims band -->
    <rect class="claims-band" x="0" y="0" width="520" height="54" fill="url(#claims-band-fill)"/>
    <text class="claims-text" x="38" y="36">ALKALINE | NO SUGAR | NO FILLERS | NO FLAVORINGS</text>

    <!-- brand -->
    <circle class="brand-dot" cx="36" cy="128" r="12" fill="var(--brand-blue)"/>
    <text class="brand-name" x="58" y="150">MARROW CREST</text>
    <text class="tagline" x="150" y="190">PERFORMANCE | HEALTH | TASTE</text>

    <!-- speed swooshes -->
    <g class="swooshes" fill="none" stroke-linecap="round">
      <path d="M300 300 C 360 250, 430 230, 520 222" stroke="var(--magenta)" stroke-width="5"/>
      <path d="M330 296 C 390 262, 450 250, 520 246" stroke="var(--violet)" stroke-width="3"/>
      <path d="M300 548 C 350 560, 400 552, 440 540" stroke="var(--magenta)" stroke-width="4"/>
      <path d="M260 580 C 340 574, 420 556, 520 520" stroke="var(--sky-blue)" stroke-width="4"/>
    </g>

    <!-- product window -->
    <ellipse class="product-window" role="img" aria-label="Clear window showing the white salt crystals" cx="390" cy="420" rx="118" ry="122" fill="var(--salt)"/>
    <ellipse class="product-window-ring" cx="390" cy="420" rx="118" ry="122" fill="none" stroke="url(#window-ring-stroke)" stroke-width="8"/>

    <!-- base band -->
    <rect class="base-band" x="0" y="560" width="520" height="120" fill="url(#base-band-fill)"/>
    <text class="net-weight" x="26" y="640">Net.Wt.16oz (453gr)</text>

    <!-- sodium badge -->
    <polygon class="sodium-badge-accent" points="380,640 520,610 520,640 380,668" fill="var(--magenta)"/>
    <polygon class="sodium-badge" points="372,570 520,540 520,612 380,642" fill="url(#sodium-badge-fill)"/>
    <text class="badge-figure" x="400" y="614">40%</text>
    <text class="badge-label" x="400" y="632">LESS SODIUM</text>
  </svg>
</main>
</body>
</html>
```